Postcard Design

Mexican Grill quick service prepare to order fresh food. Website : www.casaverdekitchen.com.

A sample of a postcard for inspiration is attached.

Target Market(s)

University Students 20-30yrs old

Industry/Entity Type

It Service

```html
<!DOCTYPE html>
<html lang="en">
<head>
<meta charset="utf-8">
<title>Casa Verde Kitchen – Postcard</title>
<link rel="stylesheet" href="https://fonts.googleapis.com/css2?family=Roboto+Condensed:wght@400;700&family=Kalam:wght@400;700&display=swap">
<style>
  :root {
    --red: #e0262b;
    --green: #6cbd45;
    --green-light: #8fd45a;
    --ink: #2b2b2b;
    --white: #ffffff;
    --stage: #e9e6e1;
    --photo-warm: #e7b77a;
    --photo-deep: #b8743a;
    --photo-light: #f3dcb6;
  }
  * { margin: 0; padding: 0; box-sizing: border-box; }
  html, body { width: 1200px; height: 1111px; overflow: hidden; }
  body { background: var(--stage); position: relative; font-family: "Roboto Condensed", Arial, sans-serif; }

  .postcard {
    position: absolute; left: 40px; top: 193px;
    width: 1120px; height: 724px;
    background: var(--white); overflow: hidden;
    box-shadow: 0 6px 18px rgba(0,0,0,.18);
  }
  .postcard__art { position: absolute; inset: 0; }

  .brand {
    position: absolute; left: 26px; top: 32px;
    display: flex; align-items: center; gap: 8px;
    color: var(--red); font-weight: 700; font-size: 24px; line-height: 1;
    white-space: nowrap;
  }
  .brand__mark { width: 12px; height: 12px; background: var(--red); }

  .headline { position: absolute; right: 22px; top: 40px; text-align: right; }
  .headline__proximity { font-size: 40px; color: var(--ink); font-weight: 700; line-height: 1.1; }
  .headline__tagline { font-size: 58px; font-weight: 700; line-height: 1.05; letter-spacing: -0.5px; }
  .headline__tagline .fresh { color: var(--green); }
  .headline__tagline .delicious { color: var(--red); }
  .headline__address { font-size: 16px; color: var(--ink); margin-top: 6px; }

  .landmark {
    position: absolute; left: 645px; top: 222px; width: 460px; height: 100px;
  }
  .landmark svg { position: absolute; inset: 0; }
  .landmark__text {
    position: absolute; inset: 0; display: flex; align-items: center; justify-content: center;
    font-family: "Kalam", cursive; color: var(--white); font-size: 32px; white-space: nowrap;
  }

  .contact { position: absolute; left: 690px; top: 340px; width: 400px; text-align: center; }
  .contact__phone { font-size: 60px; font-weight: 700; color: var(--green); line-height: 1; }
  .contact__hours { font-family: "Kalam", cursive; font-size: 28px; color: var(--ink); margin-top: 12px; }
  .contact__hours em { font-style: normal; color: var(--red); }

  .coupon {
    position: absolute; left: 672px; top: 493px; width: 448px; height: 231px;
    background: var(--red);
  }
  .coupon__frame {
    position: absolute; left: 26px; top: 19px; right: 20px; bottom: 14px;
    border: 2px dashed rgba(255,255,255,.75);
    display: flex; flex-direction: column; align-items: center; justify-content: center;
    color: var(--white); text-align: center;
  }
  .coupon__offer { font-size: 72px; font-weight: 700; line-height: .95; letter-spacing: -1px; }
  .coupon__offer .off { color: var(--ink); }
  .coupon__expiry { font-size: 24px; font-weight: 700; color: var(--green-light); line-height: 1.1; }
  .coupon__terms { font-family: "Kalam", cursive; font-size: 23px; line-height: 1.2; }
  .coupon__fine { font-size: 16px; line-height: 1.3; margin-top: 8px; }
</style>
</head>
<body>
  <article class="postcard">
    <svg class="postcard__art" viewBox="0 0 1120 724" width="1120" height="724">
      <polygon class="stripe-red" fill="var(--red)" points="30,174 300,40 845,724 795,724 282,98 30,212"/>
      <polygon class="stripe-green" fill="var(--green)" points="0,212 258,188 712,724 668,724 240,228 0,250"/>
      <defs>
        <linearGradient id="food-tones" x1="0" y1="0" x2="1" y2="1">
          <stop offset="0" stop-color="var(--photo-light)"/>
          <stop offset=".5" stop-color="var(--photo-warm)"/>
          <stop offset="1" stop-color="var(--photo-deep)"/>
        </linearGradient>
      </defs>
      <polygon class="food-photo" role="img" aria-label="Photo of a grilled chicken burrito cut in half with tortilla chips" fill="url(#food-tones)" points="0,266 226,246 660,724 0,724"/>
    </svg>

    <div class="brand"><span class="brand__mark"></span>Casa Verde Kitchen</div>

    <header class="headline">
      <p class="headline__proximity">One block from Westridge U</p>
      <p class="headline__tagline"><span class="fresh">FAST,FRESH &amp;</span> <span class="delicious">DELICIOUS</span></p>
      <p class="headline__address">812 W. Calle Del Monte, Oak Valley In the Harvest Market Shopping Center</p>
    </header>

    <div class="landmark">
      <svg viewBox="0 0 460 100" width="460" height="100">
        <path fill="var(--red)" d="M18,30 L60,12 L200,8 L330,14 L430,20 L456,34 L420,44 L450,58 L400,70 L436,84 L300,92 L160,96 L40,88 L4,74 L30,60 L0,46 Z"/>
      </svg>
      <p class="landmark__text">Next to Corner Pharmacy</p>
    </div>

    <section class="contact">
      <p class="contact__phone">805.555.0142</p>
      <p class="contact__hours">Open Everyday <em>10:30 am to 9pm</em></p>
    </section>

    <section class="coupon">
      <div class="coupon__frame">
        <p class="coupon__offer">$3<span class="off">OFF</span></p>
        <p class="coupon__expiry">Expires 10/31/15</p>
        <p class="coupon__terms">Any purchase of $6 or more</p>
        <p class="coupon__fine">One coupon per person<br>Not valid with other offers</p>
      </div>
    </section>
  </article>
</body>
</html>
```